Driftwood Coatings of Central Florida, LLC. Start-up painting business needs a professional web desig

We have a start up painting business that would like to reach/focus on commercial clients like building contractors, HOA's, apartment complexes, etc.. We would like a residential aspect to the web design as well. We have an existing website at "trydriftwoodcoatings.com" with usable content. Have logo and color scheme attached. Use provided website ONLY as template. Add commercial services page. Can type own content when needed.

```html
<!DOCTYPE html>
<html lang="en">
<head>
<meta charset="utf-8">
<title>Driftwood Coatings of Central Florida, LLC</title>
<link href="https://fonts.googleapis.com/css2?family=Open+Sans:wght@300;400;600;700&family=Great+Vibes&display=swap" rel="stylesheet">
<style>
:root{
  --red:#bb4446;
  --red-soft:#e07b7b;
  --gold:#d9a020;
  --gold-soft:#e8b84a;
  --green:#8aa62e;
  --green-soft:#9ab83c;
  --blue:#45b5d0;
  --ink:#3d3d3d;
  --muted:#666;
  --footer:#ebebeb;
  --white:#fff;
}
*{margin:0;padding:0;box-sizing:border-box}
html,body{width:891px;height:1200px;overflow:hidden;background:var(--white)}
body{position:relative;font-family:'Open Sans',sans-serif;color:var(--ink)}
.abs{position:absolute}

.site-header{position:absolute;left:0;top:0;width:891px;height:97px;border-bottom:1px solid #e2e2e2}
.brand{left:74px;top:18px;display:flex;align-items:center;gap:12px}
.brand-mark{width:58px;height:58px;background:var(--red-soft);opacity:.85}
.brand-name{color:var(--red);font-weight:700;line-height:1.2}
.brand-name .line1{font-size:16px;display:block}
.brand-name .line2{font-size:9.5px;display:block;letter-spacing:.3px}
.call{left:515px;top:14px;display:flex;align-items:center;gap:10px;font-size:12px;font-weight:600}
.call .num{color:var(--red)}
.nav{left:346px;top:57px;width:472px;display:flex}
.nav a{flex:1;border-top:3px solid;padding-top:14px;font-size:8.5px;color:#444;text-decoration:none;padding-left:2px}
.nav a:nth-child(1){border-color:var(--red-soft)}
.nav a:nth-child(2){border-color:var(--gold-soft)}
.nav a:nth-child(3){border-color:var(--green-soft)}
.nav a:nth-child(4){border-color:var(--blue)}

.hero{left:0;top:97px;width:891px;height:341px;background:linear-gradient(90deg,#f7f6f4 0%,#eeece8 45%,#b9bcbf 70%,#8f9498 100%)}
.hero-copy{left:80px;top:62px;width:300px}
.hero-script{font-family:'Great Vibes',cursive;color:var(--red);font-size:34px;line-height:1}
.hero-lead{font-size:17px;line-height:26px;margin-top:10px;color:#333}
.hero-name{margin-top:12px;color:var(--red);font-weight:600;font-size:16.5px;line-height:20px}
.hero-sub{font-weight:300;font-size:15px;line-height:20px}
.hero-btn{display:inline-block;margin-top:20px;background:var(--blue);color:var(--white);font-size:13px;width:177px;height:37px;line-height:37px;text-align:center}
.arrow{width:30px;height:30px;top:153px}

.welcome{left:0;top:438px;width:891px;height:140px;background:var(--red);color:var(--white);text-align:center}
.welcome h1{font-size:17px;font-weight:600;margin-top:36px}
.welcome p{font-size:9.3px;line-height:20px;margin-top:10px}

.services-head{left:0;top:624px;width:891px;text-align:center}
.services-head h2{font-size:17px;font-weight:700;color:#444}
.services-head p{font-size:9px;line-height:20px;color:var(--muted);width:700px;margin:16px auto 0}
.cards{left:74px;top:736px;display:flex;gap:12px}
.card{width:177px}
.card .photo{height:100px}
.card .label{height:28px;line-height:28px;padding-left:13px;color:var(--white);font-size:8.5px;font-weight:700}

.about-photo{left:74px;top:924px;width:239px;height:140px;background:linear-gradient(135deg,#f4e7d2 0%,#e9c6c8 40%,#8a6a5a 75%,#5d4a44 100%)}
.about{left:360px;top:926px;width:440px}
.about h2{font-size:17px;font-weight:700;color:#444}
.about p{font-size:8.3px;line-height:16.5px;color:var(--muted);margin-top:12px}
.about p + p{margin-top:17px}

.site-footer{left:40px;top:1121px;width:851px;height:79px;background:var(--footer);border-top:1px solid #ddd}
.foot-links{left:34px;top:24px;font-size:8.5px;color:var(--muted);word-spacing:2px}
.foot-links span{margin:0 13px}
.copy{left:34px;top:46px;font-size:8.5px;color:var(--muted)}
.social{left:500px;top:27px;display:flex;align-items:center;gap:6px;font-size:8.5px;color:var(--muted)}
.social .dot{width:24px;height:24px;border-radius:50%}
</style>
</head>
<body>

<header class="site-header">
  <div class="abs brand">
    <div class="brand-mark"></div>
    <div class="brand-name"><span class="line1">Driftwood Coatings</span><span class="line2">OF CENTRAL FLORIDA, LLC.</span></div>
  </div>
  <div class="abs call">
    <svg width="30" height="30" viewBox="0 0 30 30" aria-hidden="true"><circle cx="15" cy="15" r="15" fill="#45b5d0"/><path d="M10.5 8.5l2.4-.4 1.3 3.3-1.6 1.2a8 8 0 0 0 3.8 3.8l1.2-1.6 3.3 1.3-.4 2.4c-.2.9-1 1.3-1.9 1.2A11 11 0 0 1 9.3 10.4c-.1-.9.3-1.7 1.2-1.9z" fill="#fff"/></svg>
    <span>Cal Us Today! <span class="num">+1.863-555-0148, +1.863-555-0172</span></span>
  </div>
  <nav class="abs nav"><a href="#">HOME</a><a href="#">ABOUT US</a><a href="#">SERVICES</a><a href="#">CONTACT US</a></nav>
</header>

<section class="abs hero" role="img" aria-label="Painter in a hard hat rolling white paint onto an exterior wall">
  <div class="abs hero-copy">
    <div class="hero-script">Where dreams meet reality</div>
    <p class="hero-lead">The best home painters are yours for the taking.</p>
    <div class="hero-name">DRIFTWOOD COATINGS</div>
    <div class="hero-sub">OF CENTRAL FLORIDA, LLC.</div>
    <a class="hero-btn">Click here for more info</a>
  </div>
  <svg class="abs arrow" style="left:22px" viewBox="0 0 30 30" aria-hidden="true"><circle cx="15" cy="15" r="15" fill="#d5d5d5"/><path d="M17.5 8l-7 7 7 7" stroke="#fff" stroke-width="4" fill="none"/></svg>
  <svg class="abs arrow" style="left:843px" viewBox="0 0 30 30" aria-hidden="true"><circle cx="15" cy="15" r="15" fill="#6f7478" opacity=".6"/><path d="M12.5 8l7 7-7 7" stroke="#555" stroke-width="4" fill="none"/></svg>
</section>

<section class="abs welcome">
  <h1>WELCOME TO DRIFTWOOD COATINGS</h1>
  <p>Driftwood Coatings of Central Florida, LLC. has painted thousands of homes in its day, but the one we're most excited about painting is the one we're painting today.<br>Your home could be that home.</p>
</section>

<section class="abs services-head">
  <h2>OUR SERVICES</h2>
  <p>We offer a wide variety of services to meet all your needs. When a project comes up no matter planned or unplanned unexpected things can happen. We take the guess work out of the way with our worry free guarantee.</p>
</section>

<div class="abs cards">
  <div class="card"><div class="photo" role="img" aria-label="Worker repairing a house exterior" style="background:linear-gradient(135deg,#c9ccd3,#b04a4e 70%,#8f3a3d)"></div><div class="label" style="background:var(--red)">REPAIR SERVICES</div></div>
  <div class="card"><div class="photo" role="img" aria-label="Living room with orange sofa and framed pictures" style="background:linear-gradient(180deg,#b98a4f,#d9a86a 60%,#e8dcc4)"></div><div class="label" style="background:var(--gold)">INTERIOR DESIGN SERVICES</div></div>
  <div class="card"><div class="photo" role="img" aria-label="Woman painting an interior wall with a roller" style="background:linear-gradient(135deg,#f1ede6,#d8cfc2 60%,#9fb9b4)"></div><div class="label" style="background:var(--green)">INTERIOR PAINTING SERVICES</div></div>
  <div class="card"><div class="photo" role="img" aria-label="Painters on ropes painting a building facade" style="background:linear-gradient(180deg,#4b8fd6,#b9d2ea 50%,#e9ecef)"></div><div class="label" style="background:var(--blue)">EXTERIOR PAINTING SERVICES</div></div>
</div>

<div class="abs about-photo" role="img" aria-label="Paint cans, brush and colour swatch fan"></div>
<section class="abs about">
  <h2>ABOUT DRIFTWOOD COATINGS</h2>
  <p>At Driftwood Coatings of Central Florida, we strive to exceed the expectations of each and every customer. We do that by using the highest quality products and through out attention to detail. You'll notice the difference immediately when you choose us to paint your home.</p>
  <p>Hiring a high-quality painting company is an important decision and we'll provide you with outstanding service--soup to nuts.</p>
</section>

<footer class="abs site-footer">
  <div class="abs foot-links">Home<span>/</span>About us<span>/</span>Services<span>/</span>Contact Us</div>
  <div class="abs copy">© 2015. Driftwood Coatings. All rights reserved.</div>
  <div class="abs social">
    <span style="margin-right:4px">Connect with our social network :</span>
    <span class="dot" style="background:#3b64b0" aria-label="Social profile"></span>
    <span class="dot" style="background:#45b5d0" aria-label="Social profile"></span>
    <span class="dot" style="background:#1f7ea6" aria-label="Social profile"></span>
    <span class="dot" style="background:#333" aria-label="Social profile"></span>
    <span class="dot" style="background:#d42a2e" aria-label="Social profile"></span>
  </div>
</footer>

</body>
</html>
```